Business Card Design Project

New business cards that encompass our new logo.
Looking for -
Name, Title, Cell Phone, Email, Address (2 lines), Main Phone, Fax, and website.
Reason: I don't like the graphics used to show phone, fax, cell, email, web, and address.....
I like the double sided cards with logo's on the back. I do not like the logos for phone, fax, cell, address, email, or web.

```html
<!DOCTYPE html>
<html lang="en">
<head>
<meta charset="utf-8">
<title>Northline Restaurant Supply – Business Cards</title>
<link rel="stylesheet" href="https://fonts.googleapis.com/css2?family=Open+Sans:wght@400;600;700&display=swap">
<style>
  :root {
    --page: #ecebe8;
    --red-light: #c95a70;
    --red: #b1334c;
    --red-deep: #9c1f38;
    --navy: #1f3473;
    --white: #ffffff;
    --ink: #2b2b2b;
    --card-w: 530px;
    --card-h: 303px;
  }
  * { margin: 0; padding: 0; box-sizing: border-box; }
  html, body {
    width: 1200px; height: 913px; overflow: hidden;
    background: var(--page);
    font-family: "Open Sans", Arial, sans-serif;
  }
  .sheet { position: relative; width: 1200px; height: 913px; }
  .card {
    position: absolute; top: 305px;
    width: var(--card-w); height: var(--card-h);
    overflow: hidden;
    box-shadow: 0 6px 18px rgba(0,0,0,.18);
  }
  /* Back side */
  .card-back {
    left: 50px;
    background: linear-gradient(160deg, var(--red-light) 0%, var(--red) 55%, var(--red-deep) 100%);
  }
  .card-back .brand {
    position: absolute; right: 48px; top: 118px;
    text-align: right;
    color: var(--white);
    font-weight: 700;
    line-height: 1.1;
  }
  .brand .brand-main { display: block; font-size: 34px; letter-spacing: 1px; }
  .brand .brand-sub { display: block; font-size: 13px; letter-spacing: 2.5px; }
  /* Front side */
  .card-front { left: 620px; background: var(--white); }
  .card-front .wave { position: absolute; inset: 0; }
  .card-front .brand {
    position: absolute; left: 28px; top: 64px;
    color: var(--navy); font-weight: 700; line-height: 1.1;
  }
  .card-front .brand .brand-main { font-size: 36px; }
  .contact {
    position: absolute; left: 28px; top: 150px;
    list-style: none; font-size: 11.5px; color: var(--ink); line-height: 1.45;
  }
  .contact li { display: flex; align-items: flex-start; gap: 6px; }
  .contact .icon { width: 11px; height: 11px; margin-top: 3px; flex: none; }
  .contact .sep { display: inline-flex; align-items: center; gap: 4px; margin-left: 8px; }
  .holder {
    position: absolute; right: 22px; top: 224px;
    text-align: right; color: var(--white);
    white-space: nowrap;
  }
  .holder .name { font-size: 15px; font-weight: 700; line-height: 1.2; }
  .holder .title { font-size: 10.5px; font-weight: 400; }
</style>
</head>
<body>
<main class="sheet">

  <section class="card card-back" aria-label="Card back">
    <div class="brand">
      <span class="brand-main">NORTHLINE</span>
      <span class="brand-sub">RESTAURANT SUPPLY</span>
    </div>
  </section>

  <section class="card card-front" aria-label="Card front">
    <svg class="wave" viewBox="0 0 530 303" width="530" height="303" aria-hidden="true">
      <defs>
        <linearGradient id="redFill" x1="0" y1="0" x2="1" y2="1">
          <stop offset="0" stop-color="#c95a70"/>
          <stop offset="1" stop-color="#a32640"/>
        </linearGradient>
      </defs>
      <path d="M530,30 C455,70 440,190 320,245 C230,285 90,292 0,296 L0,303 L530,303 Z" fill="url(#redFill)"/>
      <path d="M530,8 C440,50 430,180 300,238 C210,278 80,285 0,288" fill="none" stroke="#1f3473" stroke-width="5"/>
      <path d="M530,18 C448,60 436,188 312,243 C222,282 88,289 0,292" fill="none" stroke="#1f3473" stroke-width="2"/>
    </svg>

    <div class="brand">
      <span class="brand-main">NORTHLINE</span>
      <span class="brand-sub">RESTAURANT SUPPLY</span>
    </div>

    <ul class="contact">
      <li>
        <svg class="icon" viewBox="0 0 12 12"><rect x="3" y="0.5" width="6" height="11" rx="1.2" fill="#b1334c"/><rect x="4.2" y="2" width="3.6" height="6" fill="#fff"/></svg>
        <span>00.00.00.0000</span>
        <span class="sep"><svg class="icon" viewBox="0 0 12 12"><path d="M1 4 Q6 0 11 4 L10 6 L8 5 L8 4 Q6 3 4 4 L4 5 L2 6 Z M2.5 7 H9.5 V11 H2.5 Z" fill="#b1334c"/></svg>00.00.00.0000</span>
        <span class="sep"><svg class="icon" viewBox="0 0 12 12"><rect x="1" y="4" width="10" height="7" rx="1" fill="#b1334c"/><rect x="3" y="1" width="6" height="4" fill="#b1334c"/><rect x="3.5" y="6" width="5" height="1" fill="#fff"/></svg>00.00.00.0000</span>
      </li>
      <li>
        <svg class="icon" viewBox="0 0 12 12"><path d="M6 0.5 A4 4 0 0 1 10 4.5 C10 7.5 6 11.5 6 11.5 C6 11.5 2 7.5 2 4.5 A4 4 0 0 1 6 0.5 Z" fill="#b1334c"/><circle cx="6" cy="4.5" r="1.5" fill="#fff"/></svg>
        <span>Your Commercial or office address<br>in just two line only</span>
      </li>
      <li>
        <svg class="icon" viewBox="0 0 12 12"><rect x="0.5" y="2" width="11" height="8" fill="#b1334c"/><path d="M0.5 2 L6 6.5 L11.5 2" fill="none" stroke="#fff" stroke-width="1"/></svg>
        <span>yourname@yourwebsite.com</span>
      </li>
      <li>
        <svg class="icon" viewBox="0 0 12 12"><circle cx="6" cy="6" r="5.5" fill="#b1334c"/><path d="M0.5 6 H11.5 M6 0.5 C3 3 3 9 6 11.5 M6 0.5 C9 3 9 9 6 11.5" fill="none" stroke="#fff" stroke-width="0.8"/></svg>
        <span>www.yourwebsite.com</span>
      </li>
    </ul>

    <div class="holder">
      <p class="name">Your Long Name</p>
      <p class="title">Managing Director</p>
    </div>
  </section>

</main>
</body>
</html>
```